Packaging Design job - Natural Sleep Aid Supplement

We need a packaging design theme for a Natural Sleep Aid Supplement allowing a fall asleep fast and a good quality of sleep. This product will be in blister form of 15 capsules. We need for this a packaging design for the box.Dimensions: 75 * 25 * 116 mmThe active ingredients are: passionflower; lemon balm and valerianProduct Name: SOMNATWe would like to see clean, modern and fresh designs.This should give the impression of professional products of pharmaceutical quality.You will also find attached the logo of our company.Ps : You can change the color of the logo

Font styles to use
Serif
Sans Serif

Colors

Designer to choose colors to be used in the design.

Requirements
Should not have
• Sales and other "must buy" "guaranteed" etc

```html
<!DOCTYPE html>
<html lang="en">
<head>
<meta charset="utf-8">
<title>DORVELA – Natural Sleep Aid Supplement Box</title>
<link rel="stylesheet" href="https://fonts.googleapis.com/css2?family=Exo+2:ital,wght@1,800&family=Open+Sans:wght@400;700&display=swap">
<style>
  :root {
    --bg: #cfe0e8;
    --purple-deep: #241043;
    --purple-mid: #4f1470;
    --purple-bright: #8b1c9e;
    --ink: #3a1760;
    --grey: #e6e6e8;
    --white: #ffffff;
    --teal: #2ec4b6;
  }
  * { margin: 0; padding: 0; box-sizing: border-box; }
  html, body { width: 767px; height: 1200px; overflow: hidden; }
  body { background: var(--bg); font-family: "Open Sans", sans-serif; position: relative; }

  .dieline { position: absolute; inset: 0; }
  .part { position: absolute; }

  .band {
    background: linear-gradient(100deg, var(--purple-deep) 0%, var(--purple-mid) 45%, var(--purple-bright) 100%);
  }
  .band-side {
    background: linear-gradient(180deg, var(--purple-deep) 0%, var(--purple-mid) 50%, var(--purple-bright) 100%);
  }
  .paper { background: var(--white); }
  .grey-strip { background: var(--grey); }

  .brand {
    position: absolute; left: 0; right: 0; top: 16px;
    display: flex; justify-content: center; align-items: center; gap: 7px;
  }
  .brand-dot { width: 12px; height: 12px; border-radius: 50%; background: var(--teal); }
  .brand-name {
    font-family: "Open Sans", sans-serif; font-weight: 700; font-size: 22px;
    color: var(--white); letter-spacing: 0.5px;
  }

  .product-name {
    position: absolute; left: 10px;
    font-family: "Exo 2", sans-serif; font-style: italic; font-weight: 800;
    color: var(--white); line-height: 1; letter-spacing: 1px;
  }
  .product-sub {
    position: absolute; left: 12px;
    font-family: "Open Sans", sans-serif; font-weight: 700;
    font-size: 6.5px; color: var(--white); letter-spacing: 0.2px;
  }

  .ingredients {
    position: absolute; left: 14px; top: 6px; list-style: none;
    font-size: 11px; line-height: 14px; color: var(--ink);
  }
  .ingredients li::before { content: "• "; }

  .count-pill {
    position: absolute; left: 224px; top: 7px; width: 78px; height: 36px;
    border-radius: 18px;
    background: linear-gradient(100deg, var(--purple-deep), var(--purple-mid));
    color: var(--white); text-align: center;
    display: flex; flex-direction: column; justify-content: center;
  }
  .count-pill .num { font-size: 11px; font-weight: 700; line-height: 12px; }
  .count-pill .unit { font-size: 7px; font-weight: 700; line-height: 9px; }

  .side-label {
    position: absolute; left: 50%; top: 50%;
    transform: translate(-50%, -50%) rotate(90deg);
    white-space: nowrap; text-align: center;
  }
  .side-label .side-name {
    display: block; font-family: "Exo 2", sans-serif; font-style: italic; font-weight: 800;
    font-size: 36px; color: var(--white); line-height: 1;
  }
  .side-label .side-sub {
    display: block; font-weight: 700; font-size: 5.5px; color: var(--white); margin-top: 2px;
  }
</style>
</head>
<body>
<div class="dieline">

  <!-- Front panel -->
  <section class="part front-panel" style="left:222px; top:498px; width:325px; height:208px;">
    <div class="part band" style="left:0; top:0; width:325px; height:134px;">
      <div class="brand"><span class="brand-dot"></span><span class="brand-name">NOVELIA</span></div>
      <div class="product-name" style="top:72px; font-size:40px;">DORVELA</div>
      <div class="product-sub" style="top:118px;">NATURAL SLEEP AID SUPPLEMENT</div>
    </div>
    <div class="part paper" style="left:0; top:134px; width:325px; height:10px;"></div>
    <div class="part grey-strip" style="left:0; top:144px; width:325px; height:50px;">
      <ul class="ingredients"><li>Passionflower</li><li>Lemon balm</li><li>Valerian</li></ul>
      <div class="count-pill"><span class="num">15</span><span class="unit">capsules</span></div>
    </div>
    <div class="part paper" style="left:0; top:194px; width:325px; height:14px;"></div>
  </section>

  <!-- Right side flap -->
  <section class="part band-side side-flap" style="left:547px; top:498px; width:69px; height:208px;">
    <div class="side-label"><span class="side-name">DORVELA</span><span class="side-sub">NATURAL SLEEP AID SUPPLEMENT</span></div>
  </section>

  <!-- Middle top band with dust flaps -->
  <svg class="part" style="left:200px; top:706px;" width="370" height="74" viewBox="0 0 370 74" aria-hidden="true">
    <path d="M22 0 L6 4 L2 70 L22 72 Z" fill="#fff"/>
    <path d="M347 0 L363 4 L367 70 L347 72 Z" fill="#fff"/>
  </svg>
  <section class="part band top-band" style="left:222px; top:708px; width:325px; height:70px;">
    <div class="product-name" style="top:14px; font-size:30px;">DORVELA</div>
    <div class="product-sub" style="top:50px; font-size:5.5px;">NATURAL SLEEP AID SUPPLEMENT</div>
  </section>

  <!-- Back panel -->
  <section class="part back-panel" style="left:222px; top:778px; width:325px; height:210px;">
    <div class="part band" style="left:0; top:0; width:325px; height:134px;">
      <div class="brand"><span class="brand-dot"></span><span class="brand-name">NOVELIA</span></div>
      <div class="product-name" style="top:72px; font-size:40px;">DORVELA</div>
      <div class="product-sub" style="top:118px;">NATURAL SLEEP AID SUPPLEMENT</div>
    </div>
    <div class="part paper" style="left:0; top:134px; width:325px; height:10px;"></div>
    <div class="part grey-strip" style="left:0; top:144px; width:325px; height:50px;">
      <ul class="ingredients"><li>Passionflower</li><li>Lemon balm</li><li>Valerian</li></ul>
      <div class="count-pill"><span class="num">15</span><span class="unit">capsules</span></div>
    </div>
    <div class="part paper" style="left:0; top:194px; width:325px; height:16px;"></div>
  </section>

  <!-- Left side flap -->
  <section class="part band-side side-flap" style="left:152px; top:778px; width:70px; height:208px;">
    <div class="side-label"><span class="side-name">DORVELA</span><span class="side-sub">NATURAL SLEEP AID SUPPLEMENT</span></div>
  </section>

  <!-- Bottom band with dust flaps and tuck tab -->
  <svg class="part" style="left:200px; top:986px;" width="370" height="100" viewBox="0 0 370 100" aria-hidden="true">
    <path d="M22 2 L6 6 L2 70 L22 72 Z" fill="#fff"/>
    <path d="M347 2 L363 6 L367 70 L347 72 Z" fill="#fff"/>
    <path d="M22 70 L347 70 L347 86 Q345 98 330 99 L40 99 Q24 98 22 86 Z" fill="#fff"/>
  </svg>
  <section class="part band bottom-band" style="left:222px; top:988px; width:325px; height:69px;">
    <div class="product-name" style="top:14px; font-size:30px;">DORVELA</div>
    <div class="product-sub" style="top:50px; font-size:5.5px;">NATURAL SLEEP AID SUPPLEMENT</div>
  </section>

</div>
</body>
</html>
```